Business Card

We would like a very clean corporate, two sided business card that conveys that we are a quality focused, reliable organisation that can make a business better. We focus on a cycle of continuous improvement for IT systems.

The brief is primarily clean and corporate, nothing overly complicated.

We sell IT services, IT support, server implementation, problem solving services to businesses in Australia.

Business

```html
<!DOCTYPE html>
<html lang="en">
<head>
<meta charset="utf-8">
<title>Corvane – Business Card Options</title>
<link rel="stylesheet" href="https://fonts.googleapis.com/css2?family=Arimo:wght@400;700&display=swap">
<style>
  :root {
    --pink-deep: #e6195a;
    --pink-mid: #ee4a6a;
    --pink-soft: #f58a8f;
    --pink-pale: #fbd3d8;
    --ink: #222222;
    --ink-soft: #3a3a3a;
    --paper: #ffffff;
    --paper-grey: #f1f1f1;
    --edge: #9a9a9a;
  }
  * { margin: 0; padding: 0; box-sizing: border-box; }
  html, body { width: 1200px; height: 1044px; overflow: hidden; background: var(--paper); }
  body { position: relative; font-family: "Arimo", Arial, sans-serif; color: var(--ink); }

  .card { position: absolute; width: 543px; height: 302px; overflow: hidden; border: 1px solid var(--edge); background: var(--paper); }
  .card--row1 { top: 0; }
  .card--row2 { top: 360px; }
  .card--row3 { top: 740px; background: linear-gradient(180deg, var(--paper) 0%, var(--paper-grey) 100%); }
  .card--front { left: 0; }
  .card--back { left: 657px; }
  .card--solid { border: none; background: linear-gradient(90deg, var(--pink-deep) 0%, var(--pink-mid) 55%, var(--pink-soft) 100%); }

  .wordmark { position: absolute; display: flex; align-items: center; gap: 14px; }
  .wordmark__name { font-size: 52px; font-weight: 400; letter-spacing: -1px; color: var(--ink-soft); }
  .wordmark__dot { width: 22px; height: 22px; border-radius: 50%; background: var(--pink-deep); }

  .details { position: absolute; left: 0; right: 0; text-align: center; font-size: 15px; line-height: 1.35; }
  .details--framed { left: 24px; right: 24px; font-size: 13.5px; }
  .contact-row { position: absolute; left: 24px; right: 24px; display: flex; justify-content: space-between; font-size: 15px; }
  .contact-row--framed { left: 30px; right: 30px; font-size: 14px; }

  .band { position: absolute; left: 0; right: 0; bottom: 0; height: 92px; }
  .band--contact { background: linear-gradient(90deg, var(--pink-deep) 0%, var(--pink-mid) 60%, var(--pink-soft) 100%); }
  .band--services { background: linear-gradient(90deg, var(--pink-pale) 0%, var(--pink-soft) 45%, var(--pink-deep) 100%); }
  .band .details, .band .contact-row { font-size: 12.5px; font-weight: 700; color: var(--ink); }

  .it-mark { position: absolute; line-height: 0.8; font-weight: 400; white-space: nowrap; }
  .services { position: absolute; list-style: none; white-space: nowrap; }

  .edge-strip { position: absolute; top: 0; width: 16px; height: 100%; }
  .edge-strip--left { left: 0; }
  .edge-strip--right { right: 0; }
</style>
</head>
<body>

  <section class="card card--row1 card--front">
    <div class="wordmark" style="left:152px; top:68px;">
      <span class="wordmark__name">corvane</span><span class="wordmark__dot"></span>
    </div>
    <p class="details" style="top:214px;">Corvane Pty Ltd,Suite 210, 14-18 Harbour Lane,Kirribilli Heights, NSW, 2061<br>Australia</p>
    <div class="contact-row" style="top:264px;">
      <span>PH: +61 2 5550 1840</span><span>FAX: +61 2 5550 1847</span><span>ABN: 48 115 330 276</span>
    </div>
  </section>

  <section class="card card--row1 card--back card--solid">
    <span class="it-mark" style="left:38px; top:82px; font-size:190px; letter-spacing:-8px; color:var(--paper);">IT</span>
    <ul class="services" style="left:256px; top:78px; font-size:27px; line-height:56px; color:var(--paper); text-align:center; width:260px;">
      <li>Consulting</li><li>OutSourcing</li><li>Managed Services</li>
    </ul>
  </section>

  <section class="card card--row2 card--front">
    <div class="wordmark" style="left:122px; top:62px;">
      <span class="wordmark__name">corvane</span><span class="wordmark__dot"></span>
    </div>
    <div class="band band--contact">
      <p class="details" style="top:12px;">Corvane Pty Ltd,Suite 210, 14-18 Harbour Lane,Kirribilli Heights, NSW, 2061<br>Australia</p>
      <div class="contact-row" style="top:62px; left:14px; right:30px;">
        <span>PH: +61 2 5550 1840</span><span>FAX: +61 2 5550 1847</span><span>ABN: 48 115 330 276</span>
      </div>
    </div>
  </section>

  <section class="card card--row2 card--back">
    <div class="wordmark" style="left:140px; top:60px;">
      <span class="wordmark__name">corvane</span><span class="wordmark__dot"></span>
    </div>
    <div class="band band--services">
      <span class="it-mark" style="left:22px; top:14px; font-size:86px; color:var(--ink);">IT</span>
      <ul class="services" style="left:112px; top:8px; font-size:21px; line-height:26px; color:var(--ink);">
        <li>Consulting</li><li>OutSourcing</li><li>Managed Service</li>
      </ul>
    </div>
  </section>

  <section class="card card--row3 card--front">
    <svg class="edge-strip edge-strip--left" viewBox="0 0 16 302" preserveAspectRatio="none" aria-hidden="true">
      <polygon points="0,0 14,28 14,274 0,302" fill="var(--pink-deep)"/>
    </svg>
    <svg class="edge-strip edge-strip--right" viewBox="0 0 16 302" preserveAspectRatio="none" aria-hidden="true">
      <polygon points="16,0 2,28 2,274 16,302" fill="var(--pink-deep)"/>
    </svg>
    <div class="wordmark" style="left:138px; top:26px;">
      <span class="wordmark__name">corvane</span><span class="wordmark__dot"></span>
    </div>
    <p class="details details--framed" style="top:204px;">Corvane Pty Ltd,Suite 210, 14-18 Harbour Lane,Kirribilli Heights, NSW, 2061<br>Australia</p>
    <div class="contact-row contact-row--framed" style="top:265px;">
      <span>PH: +61 2 5550 1840</span><span>FAX: +61 2 5550 1847</span><span>ABN: 48 115 330 276</span>
    </div>
  </section>

  <section class="card card--row3 card--back">
    <svg class="edge-strip edge-strip--left" viewBox="0 0 16 302" preserveAspectRatio="none" aria-hidden="true">
      <polygon points="0,0 14,28 14,274 0,302" fill="var(--pink-deep)"/>
    </svg>
    <svg class="edge-strip edge-strip--right" viewBox="0 0 16 302" preserveAspectRatio="none" aria-hidden="true">
      <polygon points="16,0 2,28 2,274 16,302" fill="var(--pink-deep)"/>
    </svg>
    <div class="wordmark" style="left:52px; top:10px;">
      <span class="wordmark__name">corvane</span><span class="wordmark__dot"></span>
    </div>
    <span class="it-mark" style="left:46px; top:124px; font-size:140px; letter-spacing:-6px; color:var(--pink-mid);">IT</span>
    <ul class="services" style="left:180px; top:132px; font-size:27px; line-height:38px; color:var(--ink);">
      <li>Consulting</li><li>Outsourcing</li><li>Managed Services</li>
    </ul>
  </section>

</body>
</html>
```